Quorvex business card design

create modern and tech looking business card that is clean but effectively communciates that we are a cloud communications company.
Should have at minimum:
Employee Name
Postion
Phone Number
Email
website
create modern and tech looking business card that is clean but effectively communciates that we are a cloud communications company. We have two logo color schemes (attached) so would like to see designs both ways
Should have at minimum:
Employee Name
Postion
Phone Number
Email
website

```html
<!DOCTYPE html>
<html lang="en">
<head>
<meta charset="UTF-8">
<title>Quorvex business card</title>
<link href="https://fonts.googleapis.com/css2?family=Cormorant+Garamond:wght@400;500;600&display=swap" rel="stylesheet">
<style>
  :root {
    --backdrop: #3e3e3e;
    --card-black: #040404;
    --card-white: #f7f7f7;
    --accent-cyan: #27a9cc;
    --accent-purple: #6a2e91;
    --text-light: #f2f2f2;
    --text-dark: #3a3a3a;
    --serif: "Cormorant Garamond", Georgia, serif;
  }
  * { box-sizing: border-box; margin: 0; padding: 0; }
  html, body { width: 1200px; height: 1000px; overflow: hidden; }
  body {
    background: var(--backdrop);
    display: flex; flex-direction: column; align-items: center; justify-content: center;
    gap: 44px; font-family: var(--serif);
  }
  .card {
    width: 760px; height: 434px; position: relative; overflow: hidden;
    box-shadow: 0 12px 30px rgba(0,0,0,.45);
  }
  /* Back side */
  .card--back { background: var(--card-black); }
  .edge-right {
    position: absolute; top: 0; right: 0; width: 10px; height: 100%;
  }
  .edge-right .dashes {
    position: absolute; top: 0; right: 0; width: 10px; height: 190px;
    background: repeating-linear-gradient(to bottom, var(--accent-cyan) 0 6px, transparent 6px 14px);
  }
  .edge-right .line {
    position: absolute; top: 190px; right: 0; width: 4px; bottom: 0; background: var(--accent-cyan);
  }
  .edge-bottom {
    position: absolute; left: 0; bottom: 0; width: 100%; height: 10px;
  }
  .edge-bottom .dashes {
    position: absolute; left: 0; bottom: 0; width: 440px; height: 10px;
    background: repeating-linear-gradient(to right, var(--accent-cyan) 0 6px, transparent 6px 14px);
  }
  .edge-bottom .line {
    position: absolute; left: 440px; right: 0; bottom: 0; height: 4px; background: var(--accent-cyan);
  }
  .brand {
    position: absolute; display: flex; align-items: center; gap: 14px;
  }
  .brand__dot { width: 44px; height: 44px; border-radius: 50%; background: var(--accent-purple); }
  .brand__name {
    font-family: var(--serif); font-weight: 600; font-size: 46px; letter-spacing: 3px;
  }
  .card--back .brand { left: 50%; top: 50%; transform: translate(-50%, -60%); }
  .card--back .brand__name { color: #5a5a5a; }

  /* Front side */
  .card--front { display: flex; background: var(--card-white); }
  .front__logo-side {
    width: 48%; position: relative;
    background: linear-gradient(120deg, #ffffff 0%, #f1f1f1 100%);
  }
  .front__logo-side .brand { left: 50%; top: 52%; transform: translate(-50%, -50%); }
  .front__logo-side .brand__name { color: var(--text-dark); }
  .front__info-side {
    width: 52%; background: var(--card-black); color: var(--text-light);
    padding: 52px 0 0 60px;
  }
  .person__name { font-size: 40px; font-weight: 400; line-height: 1; }
  .person__name .first { color: var(--accent-cyan); }
  .person__role { font-size: 14px; margin-top: 2px; }
  .contact { list-style: none; margin-top: 48px; }
  .contact__item {
    display: flex; align-items: center; gap: 14px; font-size: 19px; margin-bottom: 17px;
  }
  .contact__icon {
    width: 28px; height: 28px; border-radius: 50%; background: var(--accent-cyan);
    display: flex; align-items: center; justify-content: center; flex-shrink: 0;
  }
  .contact__icon svg { width: 15px; height: 15px; }
</style>
</head>
<body>
  <section class="card card--back" aria-label="Card back">
    <div class="brand">
      <span class="brand__dot"></span>
      <span class="brand__name">QUORVEX</span>
    </div>
    <div class="edge-right"><span class="dashes"></span><span class="line"></span></div>
    <div class="edge-bottom"><span class="dashes"></span><span class="line"></span></div>
  </section>

  <section class="card card--front" aria-label="Card front">
    <div class="front__logo-side">
      <div class="brand">
        <span class="brand__dot"></span>
        <span class="brand__name">QUORVEX</span>
      </div>
    </div>
    <div class="front__info-side">
      <h1 class="person__name"><span class="first">Employee</span> Name</h1>
      <p class="person__role">Position</p>
      <ul class="contact">
        <li class="contact__item">
          <span class="contact__icon"><svg viewBox="0 0 24 24"><path fill="#050505" d="M6.6 10.8a15 15 0 0 0 6.6 6.6l2.2-2.2a1 1 0 0 1 1-.25 11.4 11.4 0 0 0 3.6.57 1 1 0 0 1 1 1V20a1 1 0 0 1-1 1A17 17 0 0 1 3 4a1 1 0 0 1 1-1h3.5a1 1 0 0 1 1 1c0 1.25.2 2.45.57 3.57a1 1 0 0 1-.25 1z"/></svg></span>
          +00 111 222 333
        </li>
        <li class="contact__item">
          <span class="contact__icon"><svg viewBox="0 0 24 24"><rect x="3" y="5" width="18" height="14" rx="1.5" fill="#050505"/><path d="M3.5 6l8.5 7 8.5-7" stroke="#27a9cc" stroke-width="1.8" fill="none"/></svg></span>
          info@yourmail.com
        </li>
        <li class="contact__item">
          <span class="contact__icon"><svg viewBox="0 0 24 24"><path fill="#050505" d="M12 2a7 7 0 0 0-7 7c0 5.2 7 13 7 13s7-7.8 7-13a7 7 0 0 0-7-7zm0 9.5A2.5 2.5 0 1 1 12 6.5a2.5 2.5 0 0 1 0 5z"/></svg></span>
          Your Address
        </li>
        <li class="contact__item">
          <span class="contact__icon"><svg viewBox="0 0 24 24" fill="none" stroke="#050505" stroke-width="2"><circle cx="12" cy="12" r="9"/><path d="M3 12h18M12 3c3 3.2 3 14.8 0 18M12 3c-3 3.2-3 14.8 0 18"/></svg></span>
          www.yourwebsite.com
        </li>
      </ul>
    </div>
  </section>
</body>
</html>
```